Velmora Biz Card 2019

New business card for Velmora Property Inspections. We are a residential home inspection company in Arizona.

Target Market(s)

Real Estate

Font styles to use
Sans Serif

Requirements
Must have
• Glen Mirewick
• Home Inspector
• Velmora Property Inspections, LLC
• 480-555-0172
• glen@velmora-llc.example

```html
<!DOCTYPE html>
<html lang="en">
<head>
<meta charset="utf-8">
<title>Velmora Biz Card 2019</title>
<link href="https://fonts.googleapis.com/css2?family=Montserrat:wght@600&family=Oswald:wght@500&family=Open+Sans:wght@400&display=swap" rel="stylesheet">
<style>
  :root {
    --page-bg: #e4e4e4;
    --brand-green: #2fb844;
    --brand-green-deep: #10a83a;
    --brand-lime: #8fd13c;
    --ink-gray: #5b5d60;
    --text-gray: #6b6d70;
    --skyline-light: #ececec;
    --skyline-mid: #d6d6d6;
    --card-white: #ffffff;
  }
  * { box-sizing: border-box; margin: 0; padding: 0; }
  html, body { width: 1200px; height: 1200px; overflow: hidden; }
  body {
    background: var(--page-bg);
    position: relative;
    font-family: "Open Sans", sans-serif;
  }
  .card {
    position: absolute;
    left: 180px;
    width: 840px;
    height: 480px;
    overflow: hidden;
    box-shadow: 0 6px 18px rgba(0,0,0,0.12);
  }
  .card-front { top: 90px; }
  .card-back { top: 630px; background: var(--card-white); }

  /* Front */
  .front-skyline {
    position: absolute; inset: 0;
    background:
      radial-gradient(ellipse at 45% 55%, var(--brand-lime) 0%, rgba(143,209,60,0) 55%),
      linear-gradient(180deg, var(--brand-green-deep) 0%, #3cb63a 45%, #2fae3b 70%, var(--brand-green-deep) 100%);
  }
  .front-content {
    position: absolute; inset: 0;
    display: flex; flex-direction: column; align-items: center; justify-content: center;
    gap: 34px;
  }
  .brand-name {
    font-family: "Montserrat", sans-serif;
    font-weight: 600;
    letter-spacing: 3px;
    display: flex; align-items: center; gap: 16px;
    white-space: nowrap;
  }
  .brand-name .mark-dot {
    width: 22px; height: 22px; border-radius: 50%;
    background: currentColor;
  }
  .front-content .brand-name { color: #fff; font-size: 58px; }
  .website {
    font-family: "Oswald", sans-serif;
    font-weight: 500;
    color: #fff;
    font-size: 24px;
    letter-spacing: 2.5px;
  }

  /* Back */
  .back-skyline {
    position: absolute; left: 0; top: 0; width: 100%; height: 300px;
    background: linear-gradient(180deg, #f3f3f3 0%, var(--skyline-light) 40%, var(--skyline-mid) 100%);
  }
  .back-brand {
    position: absolute; left: 0; right: 0; top: 110px;
    display: flex; justify-content: center;
  }
  .back-brand .brand-name { color: var(--ink-gray); font-size: 56px; }
  .back-brand .mark-dot { background: var(--brand-green); }
  .identity {
    position: absolute; left: 110px; top: 330px;
    text-align: right; width: 280px;
  }
  .person-name {
    font-family: "Oswald", sans-serif; font-weight: 500;
    color: var(--ink-gray); font-size: 34px; letter-spacing: 0.5px;
    line-height: 1.1;
  }
  .person-role {
    color: var(--brand-green); font-size: 20px; margin-top: 2px;
  }
  .divider {
    position: absolute; left: 420px; top: 318px;
    width: 2px; height: 96px; background: #c9c9c9;
  }
  .contact-list {
    position: absolute; left: 450px; top: 318px; right: 30px;
    list-style: none;
    display: flex; flex-direction: column; gap: 10px;
  }
  .contact-item {
    display: flex; align-items: center; gap: 12px;
    color: var(--text-gray); font-size: 16px;
    white-space: nowrap;
  }
  .contact-icon {
    width: 24px; height: 24px; flex: none;
  }
</style>
</head>
<body>

<section class="card card-front">
  <div class="front-skyline" role="img" aria-label="Green-toned photograph of a city skyline at dusk reflected on water"></div>
  <div class="front-content">
    <div class="brand-name"><span class="mark-dot"></span>VELMORA</div>
    <div class="website">WWW.VELMORA-LLC.EXAMPLE</div>
  </div>
</section>

<section class="card card-back">
  <div class="back-skyline" role="img" aria-label="Faded grayscale photograph of a city skyline"></div>
  <div class="back-brand">
    <div class="brand-name"><span class="mark-dot"></span>VELMORA</div>
  </div>

  <div class="identity">
    <div class="person-name">GLEN MIREWICK</div>
    <div class="person-role">Home Inspector</div>
  </div>

  <div class="divider"></div>

  <ul class="contact-list">
    <li class="contact-item">
      <svg class="contact-icon" viewBox="0 0 24 24" aria-hidden="true">
        <circle cx="12" cy="12" r="12" fill="var(--brand-green)"/>
        <path d="M7 10.5c0-1.5 2.2-2.5 5-2.5s5 1 5 2.5l-1.5 1-1.5-1v-1h-4v1l-1.5 1z M8.5 13h7l1 3h-9z" fill="#fff"/>
      </svg>
      <span>480-555-0172</span>
    </li>
    <li class="contact-item">
      <svg class="contact-icon" viewBox="0 0 24 24" aria-hidden="true">
        <circle cx="12" cy="12" r="12" fill="var(--brand-green)"/>
        <rect x="6.5" y="8" width="11" height="8" fill="none" stroke="#fff" stroke-width="1.4"/>
        <path d="M6.5 8l5.5 4.5L17.5 8" fill="none" stroke="#fff" stroke-width="1.4"/>
      </svg>
      <span>glen@velmora-llc.example</span>
    </li>
    <li class="contact-item">
      <svg class="contact-icon" viewBox="0 0 24 24" aria-hidden="true">
        <circle cx="12" cy="12" r="12" fill="var(--brand-green)"/>
        <path d="M12 5.5a4 4 0 0 1 4 4c0 3-4 8-4 8s-4-5-4-8a4 4 0 0 1 4-4z" fill="#fff"/>
        <circle cx="12" cy="9.5" r="1.6" fill="var(--brand-green)"/>
      </svg>
      <span>4410 S. Ridgeline Ave. Larkmoor, AZ 85099</span>
    </li>
  </ul>
</section>

</body>
</html>
```